Single page 8 1/2 x 11 flyer to entice new homeowners to visit our WEBSITE

A single page flyer that we can put on an easel that promotes our website, brightpantry88.com, to new homeowners for blinds, shades, bath hardware, cabinet organization, etc. This piece will be on an easel in sales centers, design studios and closing offices. We want the homeowners to know where they can go to get reliable products and service from a trusted partner of their builder for products that were not installed in their new home before they closed.

Enter the coupon code KPW10 to get 10% off of your entire purchase and free shipping. The product on our website will put the finishing touches on their home. ....make your house your home

Target Market(s)

New homebuyers

Industry/Entity Type

Residential Construction

Font styles to use
Serif

Colors
ec1f27

Requirements
Must have
• Logo and website, brightpantry88.com and tagline, make your house your home
Nice to have
• what will drive new homeowners to the website to purchase items they did not purchase before closing like window blinds and shades, bath hardware, ceiling fans, grills, electric fireplaces, etc.

```html
<!DOCTYPE html>
<html lang="en">
<head>
<meta charset="utf-8">
<title>Bright Pantry 88 – Make Your House Your Home</title>
<link rel="stylesheet" href="https://fonts.googleapis.com/css2?family=Anton&family=Lato:wght@400;700;900&family=Noto+Serif:wght@700&display=swap">
<style>
  :root {
    --brand-red: #ec1f27;
    --deep-red: #b5121a;
    --charcoal: #2b2b2d;
    --ink: #1c1c1c;
    --paper: #ffffff;
    --backdrop: #e4e3e1;
    --ring-grey: #9a9a9a;
    --sky: #dfe8f0;
    --lawn: #5f9a3c;
    --roof: #a8323a;
  }
  * { margin: 0; padding: 0; box-sizing: border-box; }
  html, body { width: 1200px; height: 865px; overflow: hidden; background: var(--backdrop); }
  .canvas { position: relative; width: 1200px; height: 865px; }
  .flyer {
    position: absolute; left: 283px; top: 22px; width: 634px; height: 820px;
    background: var(--paper); overflow: hidden;
    box-shadow: 0 4px 14px rgba(0,0,0,.18);
  }
  .house-photo {
    position: absolute; inset: 0 0 auto 0; height: 520px;
    background: linear-gradient(180deg, var(--sky) 0%, #c9d3dc 28%, #8a95a3 45%, var(--roof) 52%, #7f8c98 62%, var(--lawn) 82%, #4f8a30 100%);
    clip-path: polygon(0 0, 100% 0, 100% 515px, 0 345px);
  }
  .logo-plate {
    position: absolute; left: 0; top: 0; width: 250px; height: 130px;
    background: linear-gradient(135deg, #fff 60%, rgba(255,255,255,0) 100%);
  }
  .shapes { position: absolute; inset: 0; }
  .logo {
    position: absolute; left: 30px; top: 34px; display: flex; align-items: center; gap: 10px;
  }
  .logo-dot { width: 46px; height: 46px; border-radius: 50%; background: var(--brand-red); }
  .logo-name {
    font-family: "Lato", sans-serif; font-weight: 900; font-size: 22px; line-height: 1.05;
    color: var(--charcoal); text-transform: uppercase; width: 130px;
  }
  .offer-badge {
    position: absolute; left: 45px; top: 338px; width: 164px; height: 164px; border-radius: 50%;
    background: var(--paper); border: 8px solid #d9d9d9; outline: 2px solid var(--ring-grey);
    display: flex; flex-direction: column; align-items: center; justify-content: center; text-align: center;
    font-family: "Noto Serif", serif; font-weight: 700; box-shadow: 0 3px 8px rgba(0,0,0,.3);
  }
  .offer-amount { color: var(--brand-red); font-size: 30px; line-height: 1; letter-spacing: -1px; }
  .offer-amount small { font-size: 24px; }
  .offer-detail { color: var(--ink); font-size: 17px; line-height: 1.15; margin-top: 4px; }
  .intro {
    position: absolute; left: 28px; top: 512px; width: 285px;
    font-family: "Lato", sans-serif; font-size: 10.6px; line-height: 1.38; color: var(--ink); text-align: justify;
  }
  .intro .accent { color: var(--brand-red); }
  .tagline-lead {
    position: absolute; right: 18px; top: 526px;
    font-family: "Anton", sans-serif; font-size: 46px; line-height: 1; color: var(--paper); letter-spacing: .5px;
  }
  .tagline-main {
    position: absolute; right: 18px; top: 596px;
    font-family: "Anton", sans-serif; font-size: 84px; line-height: 1; color: var(--brand-red);
  }
  .tagline-end {
    position: absolute; right: 18px; top: 684px;
    font-family: "Anton", sans-serif; font-size: 46px; line-height: 1; color: var(--ink);
  }
  .kitchen-frame {
    position: absolute; left: 0; top: 620px; width: 312px; height: 182px; background: var(--charcoal);
  }
  .kitchen-photo {
    position: absolute; left: 28px; top: 633px; width: 268px; height: 154px;
    border: 3px solid var(--paper);
    background: linear-gradient(180deg, #e9eced 0%, #c4c9cc 45%, #8c8f92 70%, #5c5048 100%);
  }
  .call-bar {
    position: absolute; left: 312px; top: 738px; width: 322px; height: 38px; background: var(--charcoal);
    display: flex; align-items: center; justify-content: center;
    font-family: "Lato", sans-serif; font-weight: 700; font-size: 21px; color: var(--paper);
  }
  .site-url {
    position: absolute; left: 312px; top: 776px; width: 322px; height: 24px;
    display: flex; align-items: center; justify-content: center;
    font-family: "Lato", sans-serif; font-weight: 700; font-size: 15px; color: var(--ink); letter-spacing: 1.5px;
  }
  .base-stripe {
    position: absolute; left: 0; bottom: 0; width: 634px; height: 20px;
    background: linear-gradient(180deg, var(--brand-red), var(--deep-red));
  }
</style>
</head>
<body>
<main class="canvas">
  <article class="flyer">
    <div class="house-photo" role="img" aria-label="Photo of a large Victorian house with red roofs, a turret and a landscaped lawn"></div>
    <div class="logo-plate"></div>

    <svg class="shapes" width="634" height="820" viewBox="0 0 634 820" aria-hidden="true">
      <polygon points="0,345 634,515 634,531 0,361" fill="#ec1f27"/>
      <polygon points="0,361 300,441 0,470" fill="#2b2b2d"/>
      <polygon points="200,399 634,515 634,592 300,592" fill="#ec1f27"/>
      <polygon points="200,399 634,515 634,522 212,406" fill="#b5121a"/>
    </svg>

    <div class="logo">
      <span class="logo-dot"></span>
      <span class="logo-name">Bright Pantry 88</span>
    </div>

    <div class="offer-badge">
      <span class="offer-amount">10%<small>off</small></span>
      <span class="offer-detail">your entire<br>purchase!</span>
    </div>

    <p class="intro">Your builder and their trusted suppliers have partnered together to offer you this special opportunity. Go to www.brightpantry88.com and shop for your window coverings, ceiling fans, cabinet and closet organization, bath hardware and more. During Checkout, enter promo code <span class="accent">KPW10</span> and get a <span class="accent">10% discount</span> on your entire purchase!</p>

    <h1>
      <span class="tagline-lead">MAKE YOUR</span>
      <span class="tagline-main">HOUSE</span>
      <span class="tagline-end">YOUR HOME</span>
    </h1>

    <div class="kitchen-frame"></div>
    <div class="kitchen-photo" role="img" aria-label="Photo of a bright modern kitchen with organised cabinets and an island"></div>

    <div class="call-bar">Call us: (555) 014-2286</div>
    <div class="site-url">www.brightpantry88.com</div>
    <div class="base-stripe"></div>
  </article>
</main>
</body>
</html>
```